Business Card Design

Non-profit organization creating opportunities for:
Personal empowerment
Community Outreach
Healthier Life Choices
Body/Mind/Spirit Nourishment
Emotional Transformation
Charity & Network Opportunities
Everyday people making An extrodinary sufferance
All achieved from the Source within YOU.
Organization logo is the ying yang symbol with a small circle above it as if it were the head and the ying yang symbol was the body.  Also in side upper ying needs to be a heart and in the lower yang needs to be the letter C. This is very important as it came to me in a dream n the forming of this organization.  Color choice is open although a thought I hade was that the heart is red metallic foil (sine a red heart is the symbol of love)and the c is gold foil( the gifts of the 3 wise men and gold being one of them).a verticle card is preferred and logo as large as possible on it even if ying yang is made oval Ilook forward to the layouts and designs you can come up with.

Industry/Entity Type
Business
Contact Information for Business Card
Lumina Harbor. Org
Peter Galvany
Executive Director
Lumina harbor.peter@mailbrook.net
315-482-9063

```html
<!DOCTYPE html>
<html lang="en">
<head>
<meta charset="utf-8">
<title>Lumina Harbor – Business Card</title>
<link href="https://fonts.googleapis.com/css2?family=Alegreya+Sans+SC:wght@800&family=Josefin+Sans:wght@300;400&family=Montserrat:wght@700&display=swap" rel="stylesheet">
<style>
  :root{
    --backdrop:#e9e6e1;
    --teal-light:#12808a;
    --teal-dark:#0a5862;
    --orange:#f0921e;
    --red:#b3161c;
    --red-dark:#7a0d12;
    --ink-circle:#2a323d;
    --white:#ffffff;
    --mist:#cfe4e6;
    --tick:#6cc04a;
  }
  *{margin:0;padding:0;box-sizing:border-box}
  html,body{width:1200px;height:723px;overflow:hidden;background:var(--backdrop)}
  .sheet{position:relative;width:1200px;height:723px;display:flex;justify-content:center;align-items:center;gap:80px}
  .card{position:relative;width:360px;height:630px;overflow:hidden;
    background:linear-gradient(160deg,var(--teal-light),var(--teal-dark));
    box-shadow:0 8px 24px rgba(0,0,0,.25)}
  .smallcaps{font-family:"Alegreya Sans SC",sans-serif;font-weight:800;color:var(--orange);letter-spacing:.5px}

  /* front */
  .brand-disc{position:absolute;left:78px;top:28px;width:250px;height:250px;border-radius:50%;background:var(--ink-circle)}
  .brand-name{position:absolute;left:0;right:0;top:296px;text-align:center;font-size:30px}
  .rule{position:absolute;left:118px;width:220px;top:342px;border-top:3px dotted var(--red)}
  .person{position:absolute;left:60px;top:352px;font-size:40px;line-height:1}
  .role{position:absolute;left:62px;top:396px;font-family:"Montserrat",sans-serif;font-weight:700;font-size:15px;color:var(--white)}
  .swoosh{position:absolute;left:0;top:0;width:360px;height:630px}
  .contacts{position:absolute;left:116px;top:438px;list-style:none;font-family:"Josefin Sans",sans-serif;font-weight:400;font-size:15px;color:var(--white)}
  .contacts li{display:flex;align-items:center;gap:8px;margin-bottom:7px;white-space:nowrap}
  .contact-icon{width:16px;height:16px;border-radius:50%;background:var(--orange);color:var(--teal-dark);
    font:700 10px/16px "Montserrat",sans-serif;text-align:center;flex:none}

  /* back */
  .headline{position:absolute;left:0;right:0;top:34px;text-align:center;font-size:31px;line-height:1.05}
  .offer-list{position:absolute;left:26px;right:18px;top:160px;list-style:none;
    font-family:"Josefin Sans",sans-serif;font-weight:300;font-size:19px;line-height:1.25;color:var(--mist)}
  .offer-list li{position:relative;padding-left:26px;margin-bottom:3px}
  .offer-list svg{position:absolute;left:0;top:2px;width:18px;height:16px}
  .footer-mark{position:absolute;right:22px;bottom:22px;display:flex;align-items:center;gap:6px;
    font-family:"Josefin Sans",sans-serif;font-weight:400;font-size:12px;color:var(--orange)}
  .footer-mark span.dot{width:22px;height:22px;border-radius:50%;background:var(--ink-circle)}
</style>
</head>
<body>
<main class="sheet">
  <section class="card card-back" aria-label="Card back">
    <h2 class="headline smallcaps">Creating<br>opportunities<br>for:</h2>
    <ul class="offer-list">
      <li><svg viewBox="0 0 18 16"><path d="M2 8l5 5L16 3" fill="none" stroke="var(--tick)" stroke-width="3"/></svg>Personal empowerment</li>
      <li><svg viewBox="0 0 18 16"><path d="M2 8l5 5L16 3" fill="none" stroke="var(--tick)" stroke-width="3"/></svg>Community Outreach</li>
      <li><svg viewBox="0 0 18 16"><path d="M2 8l5 5L16 3" fill="none" stroke="var(--tick)" stroke-width="3"/></svg>Healthier Life Choices</li>
      <li><svg viewBox="0 0 18 16"><path d="M2 8l5 5L16 3" fill="none" stroke="var(--tick)" stroke-width="3"/></svg>Body/Mind/Spirit Nourishment</li>
      <li><svg viewBox="0 0 18 16"><path d="M2 8l5 5L16 3" fill="none" stroke="var(--tick)" stroke-width="3"/></svg>Emotional Transformation</li>
      <li><svg viewBox="0 0 18 16"><path d="M2 8l5 5L16 3" fill="none" stroke="var(--tick)" stroke-width="3"/></svg>Charity &amp; Network Opportunities</li>
      <li><svg viewBox="0 0 18 16"><path d="M2 8l5 5L16 3" fill="none" stroke="var(--tick)" stroke-width="3"/></svg>Everyday people making an extrodinary sufferance</li>
      <li><svg viewBox="0 0 18 16"><path d="M2 8l5 5L16 3" fill="none" stroke="var(--tick)" stroke-width="3"/></svg>All achieved from the source within YOU</li>
    </ul>
    <div class="footer-mark"><span class="dot"></span>Lumina Harbor</div>
  </section>

  <section class="card card-front" aria-label="Card front">
    <div class="brand-disc"></div>
    <svg class="swoosh" viewBox="0 0 360 630" aria-hidden="true">
      <path d="M0 480 C110 530 220 590 360 612 L360 624 C220 602 110 542 0 494 Z" fill="var(--red)"/>
      <path d="M0 494 C110 542 220 602 360 624 L360 630 C220 609 110 550 0 502 Z" fill="var(--red-dark)"/>
    </svg>
    <h1 class="brand-name smallcaps">Lumina Harbor</h1>
    <div class="rule"></div>
    <p class="person smallcaps">Peter Galvany</p>
    <p class="role">Executive Director</p>
    <ul class="contacts">
      <li><span class="contact-icon">W</span>luminaharbor.org</li>
      <li><span class="contact-icon">E</span>harbor.peter@mailbrook.net</li>
      <li><span class="contact-icon"><svg viewBox="0 0 16 16" width="16" height="16"><path d="M5 4c1 2 1 3 0 3.5.8 1.6 2 2.8 3.5 3.5.5-1 1.5-1 3.5 0l-1 2c-4 0-8-4-8-8z" fill="var(--teal-dark)"/></svg></span>315-482-9063</li>
    </ul>
  </section>
</main>
</body>
</html>
```